Brent's Business Cards

My husband is a self employed Cabinet Maker... who contracts to Building companies and clients directly.
He installs kitchesn, designs and also completes renovations and building work.

I would like a small, FUNKY, simple but eye catching design.

It needs to incorporate the following.
Custom Cabinets / Installations / Renovations / Design

Commercial and Residential

He does not have a Website or Facebook,
contact number is 0438 207 964 and email is brentkelway@mailpost.example

I would like a Grey/Silver on black, or blue covering.. I am open to colour designs?

Thank you. :-)

Target Market(s)

Building Companies
Clients
Other Trades people onsite,. to give out at job sites

Industry/Entity Type

Business

Contact Information for Business Card

Phone: 0438 207 964
Email: brentkelway@mailpost.example

Font styles to use
Sans Serif

Colors
0592cd
747474
474747
1b1b1b
85cae6

Requirements
Must have
• Funky, simple, eye catching design
• Would like use of Silver/Grey - and a colour that would complement this.
• Am open to ideas :-)
Nice to have
• We do not have a logo or picture, will leave this up to you if you think an image would be beneficial???
• Thank you.

Files

```html
<!DOCTYPE html>
<html lang="en">
<head>
<meta charset="utf-8">
<title>Brent Kelway – Business Card</title>
<link rel="stylesheet" href="https://fonts.googleapis.com/css2?family=PT+Sans:wght@700&display=swap">
<style>
  :root {
    --ink-navy: #0b1590;
    --steel-light: #ececef;
    --steel-mid: #c4c4c9;
    --steel-dark: #78787e;
    --tool-red: #5a1418;
    --tool-steel: #a9aab0;
  }
  html, body {
    margin: 0;
    padding: 0;
    overflow: hidden;
  }
  .card {
    position: relative;
    width: 1200px;
    height: 619px;
    overflow: hidden;
    font-family: "PT Sans", Tahoma, sans-serif;
    font-weight: 700;
    color: var(--ink-navy);
    background: linear-gradient(
      to bottom,
      #dedee1 0%,
      var(--steel-dark) 14%,
      var(--steel-mid) 28%,
      var(--steel-light) 42%,
      var(--steel-mid) 60%,
      var(--steel-dark) 74%,
      var(--steel-mid) 88%,
      #dcdcde 100%
    );
  }
  .tool-art {
    position: absolute;
    left: 28px;
    top: 55px;
    width: 370px;
    height: 480px;
  }
  .owner-name {
    position: absolute;
    left: 0;
    width: 1286px;
    top: 198px;
    margin: 0;
    text-align: center;
    font-size: 54px;
    line-height: 1;
  }
  .services {
    position: absolute;
    left: 0;
    width: 1372px;
    top: 284px;
    margin: 0;
    text-align: center;
    font-size: 26px;
    line-height: 1.6;
  }
  .contact {
    position: absolute;
    display: flex;
    align-items: center;
    gap: 14px;
    margin: 0;
  }
  .contact--email {
    left: 399px;
    top: 484px;
    font-size: 25px;
  }
  .contact--phone {
    left: 408px;
    top: 548px;
    font-size: 21px;
    gap: 20px;
  }
  .contact-icon {
    fill: none;
    stroke: var(--ink-navy);
    stroke-width: 2.4;
  }
  .contact-icon--solid {
    fill: var(--ink-navy);
    stroke: none;
  }
</style>
</head>
<body>
<div class="card">
  <svg class="tool-art" viewBox="0 0 370 480" role="img" aria-label="Illustration of a fanned set of screwdrivers with dark red handles and steel shafts">
    <defs>
      <linearGradient id="toolFill" x1="0" y1="0" x2="1" y2="1">
        <stop offset="0" stop-color="var(--tool-red)"/>
        <stop offset="0.45" stop-color="#6b2a2e"/>
        <stop offset="1" stop-color="var(--tool-steel)"/>
      </linearGradient>
    </defs>
    <polygon points="10,10 90,0 360,420 330,475 110,470 95,420 15,300" fill="url(#toolFill)"/>
  </svg>

  <h1 class="owner-name">Brent Kelway</h1>

  <p class="services">
    Custom Cabinets / Installations / Renovations / Design<br>
    Commercial and Residential
  </p>

  <p class="contact contact--email">
    <svg class="contact-icon" width="28" height="20" viewBox="0 0 28 20" aria-hidden="true">
      <rect x="1.5" y="1.5" width="25" height="17"/>
      <polyline points="1.5,1.5 14,11 26.5,1.5"/>
    </svg>
    <span>brentkelway@mailpost.example</span>
  </p>

  <p class="contact contact--phone">
    <svg class="contact-icon--solid" width="16" height="30" viewBox="0 0 16 30" aria-hidden="true">
      <rect x="3" y="0" width="2.5" height="6" rx="1"/>
      <rect x="0" y="5" width="16" height="25" rx="3"/>
      <rect x="3" y="8" width="10" height="7" fill="#d9d9dd"/>
    </svg>
    <span>0438 207 964</span>
  </p>
</div>
</body>
</html>
```